Pawn & Gun store business card design

Hello! We would like a new business card design for our pawn & gun store. We loan money on items of value and sell firearms, jewelry, electronics & more.

Card will need to have the following information:

Business name - Prairie Nickel Pawn & Gun
Address - 2417 Hwy 41 S. Suite B Wylie, TX 75061
Employees name - Marcus Pellen
Phone number - 972-555-0183
Email - PrairieNickelPawn@mailhaven.example
Website - PrairieNickelPawn.example

Somewhere on the card we would like it to say "Offering 10 Month Layaway!" & "We buy & loan on anything of value!". Our main store color is orange (please see logo). Logo does not have to be on the business card but it can be. Would like the back to have an area to write a note on the back. We like vintage things like old coins, collectables, firearms and more so think about this in the design. We want a business card as unique as our store!

Colors

Designer to choose colors to be used in the design.

Requirements
Nice to have
• Vintage Style

```html
<!DOCTYPE html>
<html lang="en">
<head>
<meta charset="utf-8">
<title>Prairie Nickel Pawn &amp; Gun — Business Card</title>
<link rel="stylesheet" href="https://fonts.googleapis.com/css2?family=Alegreya:wght@400;700;800&display=swap">
<style>
  :root {
    --bg: #2b2b2d;
    --brown: #3a1e13;
    --brown-line: #7a5f55;
    --brown-ornament: #4e2d21;
    --orange: #e8662a;
    --paper: #ffffff;
    --paper-ornament: #eee5e0;
    --ink: #3a1e13;
    --cream: #f4ece6;
  }
  * { box-sizing: border-box; margin: 0; padding: 0; }
  html, body { width: 1200px; height: 880px; overflow: hidden; }
  body {
    background: var(--bg);
    font-family: "Alegreya", Georgia, serif;
    position: relative;
  }
  .card { position: absolute; box-shadow: 0 10px 30px rgba(0,0,0,.45); }

  /* shared frame pieces */
  .frame-outer {
    position: absolute; inset: 16px;
    border: 2px solid var(--orange);
    outline: 1px solid var(--orange); outline-offset: -8px;
  }
  .frame-inner { position: absolute; inset: 38px; border: 1px solid var(--brown-line); }
  .corner-flourish {
    position: absolute; width: 18px; height: 18px;
    background: var(--orange); transform: rotate(45deg);
  }
  .corner-flourish.tl { left: 8px; top: 8px; }
  .corner-flourish.tr { right: 8px; top: 8px; }
  .corner-flourish.bl { left: 8px; bottom: 8px; }
  .corner-flourish.br { right: 8px; bottom: 8px; }
  .corner-scroll {
    position: absolute; width: 58px; height: 58px;
    border-bottom-right-radius: 100%;
  }
  .corner-scroll.tr { transform: scaleX(-1); }
  .corner-scroll.bl { transform: scaleY(-1); }
  .corner-scroll.br { transform: scale(-1); }

  /* ---------- front ---------- */
  .card-front {
    left: 80px; top: 142px; width: 340px; height: 595px;
    background: var(--brown); color: var(--cream);
  }
  .card-front .corner-scroll { background: var(--brown-ornament); }
  .card-front .corner-scroll.tl { left: 43px; top: 43px; }
  .card-front .corner-scroll.tr { right: 43px; top: 43px; }
  .card-front .corner-scroll.bl { left: 43px; bottom: 43px; }
  .card-front .corner-scroll.br { right: 43px; bottom: 43px; }

  .front-content {
    position: absolute; inset: 0;
    display: flex; flex-direction: column; align-items: center; justify-content: center;
    text-align: center; padding-bottom: 20px;
  }
  .brand-name {
    font-weight: 800; font-size: 25px; line-height: 1.1;
    color: var(--orange); text-transform: uppercase; letter-spacing: 1px;
  }
  .brand-name-front { margin-bottom: 44px; }
  .person-name {
    font-weight: 800; font-size: 19px; letter-spacing: 1px;
    text-transform: uppercase; color: var(--paper);
  }
  .divider { width: 56px; height: 2px; background: var(--orange); margin: 12px 0 16px; }
  .contact { list-style: none; font-size: 14px; line-height: 1.6; color: var(--cream); }

  /* ---------- back ---------- */
  .card-back {
    left: 490px; top: 270px; width: 595px; height: 340px;
    background: var(--paper); color: var(--ink);
  }
  .card-back .frame-inner { border-color: var(--ink); inset: 36px; }
  .card-back .corner-scroll { background: var(--paper-ornament); width: 66px; height: 66px; }
  .card-back .corner-scroll.tl { left: 41px; top: 41px; }
  .card-back .corner-scroll.tr { right: 41px; top: 41px; }
  .card-back .corner-scroll.bl { left: 41px; bottom: 41px; }
  .card-back .corner-scroll.br { right: 41px; bottom: 41px; }

  .back-content {
    position: absolute; inset: 0;
    display: flex; flex-direction: column; align-items: center; padding-top: 66px;
  }
  .note-title { font-weight: 800; font-size: 20px; letter-spacing: 3px; }
  .note-line { width: 340px; height: 1.5px; background: var(--ink); margin-top: 28px; }
  .note-line + .note-line { margin-top: 34px; }
  .tagline { margin-top: 16px; font-size: 14px; line-height: 1.4; text-align: center; }
  .brand-name-back { font-size: 12px; margin-top: 8px; }
</style>
</head>
<body>

<section class="card card-front" aria-label="Business card front">
  <div class="frame-outer"></div>
  <div class="frame-inner"></div>
  <div class="corner-flourish tl" role="img" aria-label="Orange corner flourish"></div>
  <div class="corner-flourish tr" role="img" aria-label="Orange corner flourish"></div>
  <div class="corner-flourish bl" role="img" aria-label="Orange corner flourish"></div>
  <div class="corner-flourish br" role="img" aria-label="Orange corner flourish"></div>
  <div class="corner-scroll tl" role="img" aria-label="Vintage scroll ornament"></div>
  <div class="corner-scroll tr" role="img" aria-label="Vintage scroll ornament"></div>
  <div class="corner-scroll bl" role="img" aria-label="Vintage scroll ornament"></div>
  <div class="corner-scroll br" role="img" aria-label="Vintage scroll ornament"></div>

  <div class="front-content">
    <h1 class="brand-name brand-name-front">Prairie Nickel<br>Pawn &amp; Gun</h1>
    <h2 class="person-name">Marcus Pellen</h2>
    <div class="divider"></div>
    <ul class="contact">
      <li>2417 Hwy 41 S. Suite B Wylie</li>
      <li>TX 75061</li>
      <li>972-555-0183</li>
      <li>PrairieNickelPawn@mailhaven.example</li>
      <li>PrairieNickelPawn.example</li>
    </ul>
  </div>
</section>

<section class="card card-back" aria-label="Business card back">
  <div class="frame-outer"></div>
  <div class="frame-inner"></div>
  <div class="corner-flourish tl" role="img" aria-label="Orange corner flourish"></div>
  <div class="corner-flourish tr" role="img" aria-label="Orange corner flourish"></div>
  <div class="corner-flourish bl" role="img" aria-label="Orange corner flourish"></div>
  <div class="corner-flourish br" role="img" aria-label="Orange corner flourish"></div>
  <div class="corner-scroll tl" role="img" aria-label="Vintage scroll ornament"></div>
  <div class="corner-scroll tr" role="img" aria-label="Vintage scroll ornament"></div>
  <div class="corner-scroll bl" role="img" aria-label="Vintage scroll ornament"></div>
  <div class="corner-scroll br" role="img" aria-label="Vintage scroll ornament"></div>

  <div class="back-content">
    <h2 class="note-title">NOTE</h2>
    <div class="note-line"></div>
    <div class="note-line"></div>
    <p class="tagline">Offering 10 Month Layaway!<br>We buy &amp; loan on anything of value!</p>
    <p class="brand-name brand-name-back">Prairie Nickel Pawn &amp; Gun</p>
  </div>
</section>

</body>
</html>
```